I would love for my business card to be fun and sophisicated. The clients are people that could afford nice well crafted wigs. These wigs are not like granny wigs. The're for women who are stylish and what to look there best especially if they are dealing with cancer are some from of hair loss. Do not want the card to appear crowded with to much information. If I need to eliminate some data, let me know.
Thanks

Industry/Entity Type

Hair

Contact Information for Business Card

L Radiant Tresses, Marianne Holt, owner, stylist

Wigs/Studio Showroom
Extensions
Hair Replacement
Private Room

24618 Crest Meadow Loop, Suite. R
Irvine, CA 90377
(949) 582-7041
Email: wigs@lradianttresses-example.com
www.lradianttresses-example.com

```html
<!DOCTYPE html>
<html lang="en">
<head>
<meta charset="utf-8">
<title>L Radiant Tresses – Business Card</title>
<link rel="stylesheet" href="https://fonts.googleapis.com/css2?family=Pinyon+Script&family=Cabin:wght@400&display=swap">
<style>
  :root {
    --card-bg: #ffffff;
    --ink: #111111;
    --accent-pink: #ee7fb4;
    --hair-dark: #141414;
    --dress-pink: #f08fc0;
    --skin-tone: #f6d3bd;
  }
  html, body {
    margin: 0;
    padding: 0;
    overflow: hidden;
    background: var(--card-bg);
  }
  .card {
    position: relative;
    width: 1200px;
    height: 685px;
    background: var(--card-bg);
    overflow: hidden;
    font-family: "Cabin", "Trebuchet MS", sans-serif;
    color: var(--ink);
  }
  .brand-name {
    position: absolute;
    left: 28px;
    top: 0;
    margin: 0;
    font-family: "Pinyon Script", cursive;
    font-weight: 400;
    font-size: 92px;
    line-height: 1.2;
    white-space: nowrap;
  }
  .contact-block {
    position: absolute;
    left: 130px;
    width: 500px;
    top: 128px;
    text-align: center;
  }
  .owner-name {
    margin: 0;
    font-size: 46px;
    font-weight: 400;
    line-height: 56px;
  }
  .owner-role {
    margin: 0 0 30px;
    font-size: 26px;
    line-height: 34px;
  }
  .address-lines {
    margin: 0;
    font-style: normal;
    font-size: 32px;
    line-height: 48.5px;
  }
  .address-lines .web-line {
    font-size: 30px;
  }
  .portrait-area {
    position: absolute;
    left: 632px;
    top: 0;
    width: 568px;
    height: 622px;
    border-radius: 0 0 0 40px;
    background:
      radial-gradient(ellipse 38% 30% at 62% 40%, var(--skin-tone) 0%, rgba(246,211,189,0) 100%),
      radial-gradient(ellipse 55% 35% at 65% 100%, var(--dress-pink) 0%, rgba(240,143,192,0) 100%),
      radial-gradient(ellipse 60% 55% at 58% 35%, var(--hair-dark) 0%, rgba(20,20,20,0) 100%);
  }
  .divider {
    position: absolute;
    left: 30px;
    top: 622px;
    width: 1170px;
    height: 3px;
    background: var(--ink);
  }
  .services {
    position: absolute;
    left: 0;
    top: 640px;
    width: 1200px;
    margin: 0;
    padding: 0;
    list-style: none;
    display: flex;
    justify-content: center;
    align-items: center;
    gap: 0;
    font-size: 33px;
    line-height: 42px;
  }
  .services li {
    display: flex;
    align-items: center;
  }
  .services li + li::before {
    content: "";
    width: 12px;
    height: 12px;
    border-radius: 50%;
    background: var(--accent-pink);
    margin: 0 16px;
  }
</style>
</head>
<body>
<div class="card">
  <h1 class="brand-name">L Radiant Tresses</h1>

  <div class="contact-block">
    <p class="owner-name">Marianne Holt</p>
    <p class="owner-role">Owner / Stylist</p>
    <address class="address-lines">
      Private Room 24618<br>
      Crest Meadow Loop<br>
      Suite, R Irvine<br>
      CA 90377<br>
      (949) 582-7041<br>
      <span class="web-line">wigs@lradianttresses-example.com</span><br>
      <span class="web-line">www.lradianttresses-example.com</span>
    </address>
  </div>

  <div class="portrait-area" role="img" aria-label="Illustration of a stylish woman with long flowing black hair, pearl necklace and pink top"></div>

  <div class="divider"></div>

  <ul class="services">
    <li>Wigs</li>
    <li>Studio Showroom</li>
    <li>Extensions</li>
    <li>Hair Replacement</li>
  </ul>
</div>
</body>
</html>
```